Truck Drivers Using App w/Jobsite Checklist

Looking for an 8" x 11" flyer that conveys to our customers (roofing contractors) that our drivers have tablets in each truck that have an app with a jobsite checklist that gives contractors less real time notifications and mistakes are caught with photos.
Should read something like this:
Ever wonder if your material has been delivered? We've got a solution for that!
All Trucks are equipped with dash-mounted tablet.
Here's what you get access to:
- Real Time Email Confirmation of Delivery
- Photos of Material Placement
- Before/After Photo of Driveway
- Material List of Products Delivered
- Homeowner Sign Off
Maybe a collage of the different photos available.
Target Market(s)
Roofing/Building Contractors
Industry/Entity Type
Roofing
Requirements
Must have
- website: www.harborfinchdepot.com
- tagline: Building Relationships, Building Trust - a Tradition Since 1905
- Photoshop format for further editing
Nice to have
- A smooth look to it.
- A collage of the photos avail on app

```html
<!DOCTYPE html>
<html lang="en">
<head>
<meta charset="utf-8">
<title>Harbor Finch Depot – Delivery Tablet Flyer</title>
<link href="https://fonts.googleapis.com/css2?family=Jost:ital,wght@0,400;0,500;0,600;1,400;1,500&display=swap" rel="stylesheet">
<style>
  :root {
    --page-bg: #e6e7e9;
    --paper: #ffffff;
    --navy: #2b2f8e;
    --royal: #1f6fb2;
    --sky: #2fa3dc;
    --deep: #0f5f9e;
    --ink: #1c1c24;
    --photo-road-top: #eef1f4;
    --photo-road-mid: #b9bec4;
    --photo-dash: #3a3c40;
  }
  * { box-sizing: border-box; margin: 0; padding: 0; }
  html, body {
    width: 1200px; height: 798px; overflow: hidden;
    background: var(--page-bg);
    font-family: "Jost", sans-serif;
  }
  .stage {
    width: 1200px; height: 798px;
    display: flex; align-items: center; justify-content: center;
  }
  .flyer-frame { width: 601px; height: 778px; position: relative; }
  .flyer {
    position: absolute; left: 0; top: 0;
    width: 707px; height: 915px;
    background: var(--paper);
    transform: scale(0.85); transform-origin: 0 0;
    overflow: hidden;
  }
  .art { position: absolute; left: 0; top: 0; }
  .tagline {
    position: absolute; left: 52px; top: 64px;
    font-style: italic; font-weight: 400;
    font-size: 28px; line-height: 33px;
    color: var(--navy); letter-spacing: 0.3px;
  }
  .brand {
    position: absolute; left: 500px; top: 62px; width: 180px;
    display: flex; align-items: center; gap: 8px;
  }
  .brand-dot { width: 22px; height: 22px; border-radius: 50%; background: var(--navy); flex: none; }
  .brand-name {
    font-weight: 600; font-size: 19px; line-height: 22px;
    color: var(--navy); letter-spacing: 0.5px;
  }
  .pitch { position: absolute; right: 22px; top: 498px; text-align: right; }
  .pitch-question {
    font-style: italic; font-size: 14.5px; line-height: 17px;
    color: var(--ink); text-transform: uppercase;
  }
  .pitch-answer {
    margin-top: 4px;
    font-weight: 600; font-size: 24px; line-height: 28.5px;
    color: var(--navy); text-transform: uppercase; letter-spacing: 0.4px;
  }
  .pitch-detail {
    font-weight: 600; font-size: 14.5px; line-height: 17.5px;
    color: var(--royal); text-transform: uppercase;
  }
  .access { position: absolute; right: 22px; top: 714px; text-align: right; }
  .access-title {
    font-size: 14px; letter-spacing: 0.6px;
    color: var(--royal); text-transform: uppercase; margin-bottom: 8px;
  }
  .access-list { list-style: none; }
  .access-list li {
    font-style: italic; font-size: 9.6px; line-height: 23px;
    color: var(--royal); text-transform: uppercase; letter-spacing: 0.3px;
    display: flex; justify-content: flex-end; align-items: center; gap: 14px;
  }
  .access-list li::after {
    content: ""; width: 0; height: 0;
    border-top: 6px solid transparent; border-bottom: 6px solid transparent;
    border-right: 7px solid var(--navy);
  }
  .website {
    position: absolute; right: 25px; top: 878px;
    font-size: 17px; color: var(--ink); letter-spacing: 0.2px;
  }
</style>
</head>
<body>
<main class="stage">
  <div class="flyer-frame">
    <article class="flyer">
      <svg class="art" width="707" height="915" viewBox="0 0 707 915" xmlns="http://www.w3.org/2000/svg">
        <defs>
          <linearGradient id="roadGrad" x1="0" y1="0" x2="0" y2="1">
            <stop offset="0" stop-color="var(--photo-road-top)"/>
            <stop offset="0.3" stop-color="#d7dbdf"/>
            <stop offset="0.5" stop-color="var(--photo-road-mid)"/>
            <stop offset="0.62" stop-color="var(--photo-dash)"/>
            <stop offset="1" stop-color="#26282b"/>
          </linearGradient>
          <linearGradient id="roofGrad" x1="0" y1="0" x2="1" y2="1">
            <stop offset="0" stop-color="#6f8fc0"/>
            <stop offset="0.45" stop-color="#c9a77f"/>
            <stop offset="1" stop-color="#4a4f5a"/>
          </linearGradient>
          <linearGradient id="workerGrad" x1="0" y1="0" x2="1" y2="0">
            <stop offset="0" stop-color="#e9eaec"/>
            <stop offset="1" stop-color="#d7e35a"/>
          </linearGradient>
          <linearGradient id="truckGrad" x1="0" y1="0" x2="0" y2="1">
            <stop offset="0" stop-color="#8fc1ea"/>
            <stop offset="0.5" stop-color="#e8ecef"/>
            <stop offset="1" stop-color="#55585c"/>
          </linearGradient>
          <linearGradient id="swooshGrad" x1="0" y1="0" x2="1" y2="1">
            <stop offset="0" stop-color="var(--royal)"/>
            <stop offset="1" stop-color="var(--deep)"/>
          </linearGradient>
        </defs>

        <path class="photo-cab" role="img" aria-label="Photo: truck cab dashboard with a mounted tablet showing a delivery form, highway ahead"
              d="M0,190 L462,190 C478,330 452,470 392,560 C312,660 170,705 0,690 Z" fill="url(#roadGrad)"/>

        <path class="swoosh-pale" d="M436,0 C520,150 505,360 430,500 C360,630 200,700 0,700 L0,730 C220,735 400,640 460,500 C520,360 525,160 448,0 Z" fill="var(--sky)"/>
        <path class="swoosh-main" d="M0,690 C200,712 360,640 432,520 C490,420 498,300 478,210 C520,380 500,560 420,700 C370,790 300,860 250,915 L0,915 Z" fill="url(#swooshGrad)"/>
        <path class="swoosh-light" d="M0,740 C170,760 330,700 420,600 C400,700 330,820 230,915 L200,915 C290,830 350,740 380,660 C280,740 140,770 0,770 Z" fill="var(--sky)" opacity="0.55"/>
        <path class="swoosh-white" d="M470,540 C450,700 380,820 300,915 L285,915 C370,815 435,700 470,540 Z" fill="#ffffff" opacity="0.9"/>

        <g class="collage">
          <circle cx="510" cy="353" r="131" fill="#ffffff" opacity="0.9"/>
          <circle cx="510" cy="353" r="127" fill="url(#roofGrad)" role="img" aria-label="Photo: roofer installing solar shingles on a roof"/>
          <circle cx="369" cy="592" r="111" fill="#ffffff" opacity="0.9"/>
          <circle cx="369" cy="592" r="107" fill="url(#workerGrad)" role="img" aria-label="Photo: delivery worker in a safety vest holding a tablet"/>
          <circle cx="142" cy="725" r="103" fill="#ffffff" opacity="0.9"/>
          <circle cx="142" cy="725" r="99" fill="url(#truckGrad)" role="img" aria-label="Photo: flatbed delivery truck with a boom crane carrying roofing material"/>
        </g>
      </svg>

      <h1 class="tagline">Building Relationships,<br>Building Trust -<br>a Tradition Since 1905</h1>

      <div class="brand">
        <span class="brand-dot"></span>
        <span class="brand-name">HARBOR FINCH DEPOT</span>
      </div>

      <section class="pitch">
        <p class="pitch-question">Ever wonder<br>if your material<br>has been delivered?</p>
        <h2 class="pitch-answer">We've got a<br>solution for<br>that!</h2>
        <p class="pitch-detail">All trucks are<br>equipped with<br>dash-mounted tablet.</p>
      </section>

      <section class="access">
        <h3 class="access-title">Here's what you get access to:</h3>
        <ul class="access-list">
          <li>Real time email confirmation of delivery</li>
          <li>Photos of material placement</li>
          <li>Before/after photo of driveway</li>
          <li>Material list of products delivered</li>
          <li>Homeowner sign off</li>
        </ul>
      </section>

      <p class="website">www.harborfinchdepot.com</p>
    </article>
  </div>
</main>
</body>
</html>
```